Website page design

Hi, I need to improve the look of my homepage and the final offer page of my website. www.Pebble7dock.com We have an orvex buyback program where we purchase used orvex products from consumers nationwide. If you would go click through a sample offer on the site, you will the last view final offer page where we give you a cash offer for you site. I would like to keep the red and white colors since my logo is red and white. Please pay attention to the information shown on the homepage now, it is important for me to show the visitors this information on the home page. I would also love to give the users a friendly and inviting look when clicking on the options of orvex products on the home page.

Target Market(s)

Orvex electronics consumers

Number of Pages Required

2 page

Requirements
Nice to have
• On the final offer page, i would love for the offer to give an exciting look for the pebble 7 dock offer, and a boring look for the orvex buy back offer. At the final offer page you will my websites offer ( Your Pebble7dock Offer ) vs ( Orvex buyback program offer ) which is my competitor.

```html
<!DOCTYPE html>
<html lang="en">
<head>
<meta charset="utf-8">
<title>Pebble7dock – Sell your used Orvex product</title>
<link rel="stylesheet" href="https://fonts.googleapis.com/css2?family=DM+Sans:wght@400;500;700&family=Inter:wght@400&display=swap">
<style>
  :root {
    --red: #d01f2f;
    --ink: #111111;
    --body: #333333;
    --white: #ffffff;
    --purple: #662d91;
    --teal: #13a89e;
    --grey: #97989c;
    --blue: #27aae1;
    --dark: #3b3a3c;
    --muted: #9a9a9c;
  }
  * { margin: 0; padding: 0; box-sizing: border-box; }
  html, body { width: 1200px; height: 2241px; overflow: hidden; background: var(--white); }
  body { position: relative; font-family: "DM Sans", sans-serif; color: var(--ink); }

  .site-header { position: absolute; top: 0; left: 0; width: 1200px; height: 79px; background: var(--red); }
  .brand { position: absolute; display: flex; align-items: center; gap: 14px; color: var(--white); font-weight: 500; letter-spacing: 0.5px; }
  .brand-square { border: 2px solid var(--white); }
  .site-header .brand { left: 91px; top: 22px; font-size: 22px; }
  .site-header .brand-square { width: 40px; height: 33px; }
  .main-nav { position: absolute; right: 89px; top: 18px; display: flex; align-items: center; gap: 20px; }
  .main-nav a { color: var(--white); text-decoration: none; font-size: 14px; font-weight: 500; }
  .main-nav .login { background: var(--white); color: var(--red); border-radius: 22px; padding: 12px 22px; margin-left: 0; }

  .hero-visual { position: absolute; top: 79px; left: 0; width: 1200px; height: 540px;
    background: linear-gradient(115deg, #ececec 0%, #fafafa 35%, #f4f4f4 55%, #d9d9d9 80%, #e9e9e9 100%); }
  .hero-visual::after { content: ""; position: absolute; left: 0; right: 0; bottom: 0; height: 90px; background: linear-gradient(to bottom, rgba(255,255,255,0), #fff); }
  .hero-copy { position: absolute; left: 91px; top: 188px; width: 420px; }
  .hero-copy h1 { font-size: 40px; line-height: 48px; font-weight: 700; color: var(--ink); }
  .hero-copy p { margin-top: 20px; font-family: "Inter", sans-serif; font-size: 15px; line-height: 22.5px; color: var(--body); width: 390px; }
  .hero-actions { display: flex; gap: 12px; margin-top: 28px; margin-left: -5px; }
  .btn { display: inline-flex; align-items: center; justify-content: center; height: 47px; border-radius: 24px; font-size: 14px; font-weight: 500; text-decoration: none; box-shadow: 0 8px 18px rgba(0,0,0,0.12); }
  .btn-primary { background: var(--red); color: var(--white); width: 159px; }
  .btn-secondary { background: var(--white); color: var(--red); width: 175px; }

  .trust-row { position: absolute; top: 660px; left: 0; width: 1200px; display: flex; justify-content: center; gap: 44px; }
  .trust-badge { height: 52px; border-radius: 6px; background: #eeeeee; }

  .section-title { position: absolute; left: 0; width: 1200px; text-align: center; font-size: 32px; line-height: 38px; font-weight: 700; color: var(--ink); }
  .quote-title { top: 810px; }

  .device-grid { position: absolute; top: 922px; left: 98px; width: 1004px; display: grid; grid-template-columns: 497px 497px; grid-template-rows: 220px 216px; gap: 9px 10px; }
  .device-tile { position: relative; overflow: hidden; color: var(--white); font-size: 21px; font-weight: 700; }
  .device-tile span { position: absolute; top: 50%; transform: translateY(-50%); }
  .device-art { position: absolute; bottom: 0; }
  .tile-slates { background: var(--purple); }
  .tile-slates span { left: 61px; }
  .tile-slates .device-art { left: 282px; width: 145px; height: 198px; background: linear-gradient(135deg, #e8e8e8, #3a6fb0 45%, #f0a890 80%); border-radius: 8px 8px 0 0; }
  .tile-desktops { background: var(--teal); }
  .tile-desktops span { right: 100px; }
  .tile-desktops .device-art { left: 50px; width: 235px; height: 200px; background: linear-gradient(135deg, #f2b33d, #d9342b 40%, #3a5fc9 70%, #d8d8d8); border-radius: 6px 6px 0 0; }
  .tile-notebooks { background: var(--grey); }
  .tile-notebooks span { left: 339px; }
  .tile-notebooks .device-art { left: 40px; width: 270px; height: 200px; background: linear-gradient(160deg, #2b2b2b, #7a7a7a 55%, #c8c8c8); border-radius: 8px 8px 0 0; }
  .tile-phones { background: var(--blue); }
  .tile-phones span { left: 59px; }
  .tile-phones .device-art { left: 213px; width: 248px; height: 190px; background: linear-gradient(160deg, #222, #c9193a 45%, #2cb5c9 85%); border-radius: 14px 14px 0 0; }

  .works-backdrop { position: absolute; top: 1690px; left: 0; width: 1200px; height: 211px; background: linear-gradient(to bottom, #ffffff, #f1f2f4 70%, #eceef1); }
  .works-title { top: 1466px; }
  .steps { position: absolute; top: 1540px; left: 127px; width: 946px; display: grid; grid-template-columns: repeat(3, 1fr); gap: 20px; text-align: center; }
  .step svg { width: 80px; height: 76px; stroke: var(--red); fill: none; stroke-width: 2.5; stroke-linejoin: round; stroke-linecap: round; }
  .step h3 { margin-top: 24px; font-size: 21px; font-weight: 700; color: var(--ink); }
  .step p { margin-top: 16px; font-family: "Inter", sans-serif; font-size: 14.5px; line-height: 25px; color: var(--body); }

  .site-footer { position: absolute; top: 1873px; left: 0; width: 1200px; height: 368px; }
  .footer-dark { position: absolute; top: 28px; left: 0; width: 1200px; height: 340px; background: var(--dark); }
  .footer-red { position: absolute; inset: 0; }
  .site-footer .brand { left: 117px; top: 95px; font-size: 28px; gap: 18px; }
  .site-footer .brand-square { width: 48px; height: 39px; }
  .footer-col { position: absolute; top: 100px; }
  .footer-col h4 { font-size: 15px; font-weight: 700; color: var(--white); margin-bottom: 13px; }
  .footer-col li { list-style: none; font-family: "Inter", sans-serif; font-size: 13px; line-height: 25px; color: var(--muted); }
  .col-contact { left: 660px; }
  .col-support { left: 857px; }
  .col-legal { left: 986px; }
  .copyright { position: absolute; left: 113px; top: 317px; font-family: "Inter", sans-serif; font-size: 12px; color: var(--white); }
  .social { position: absolute; left: 1000px; top: 314px; display: flex; gap: 15px; }
  .social span { width: 17px; height: 17px; border-radius: 50%; background: var(--white); }
</style>
</head>
<body>

<header class="site-header">
  <div class="brand"><div class="brand-square"></div>Pebble7dock</div>
  <nav class="main-nav">
    <a href="#">Home</a>
    <a href="#">Sell</a>
    <a href="#">Track</a>
    <a href="#">Join</a>
    <a href="#" class="login">Login Account</a>
  </nav>
</header>

<div class="hero-visual" role="img" aria-label="Top view of used Orvex laptop, phone and tablet on a white desk"></div>
<section class="hero-copy">
  <h1>Getting rid of a used orvex product? Sell it to us</h1>
  <p>Ei graece omittantur vel. Habeo persius scaevola qui te. Duo eu mucius nostrum. Causae docendi temporibus vel at. Usu ad postea fabellas, qui nostro iracundia ei.</p>
  <div class="hero-actions">
    <a href="#" class="btn btn-primary">Select Device</a>
    <a href="#" class="btn btn-secondary">Create an Account</a>
  </div>
</section>

<div class="trust-row">
  <div class="trust-badge" style="width:190px" role="img" aria-label="Authorized refurbisher badge"></div>
  <div class="trust-badge" style="width:88px" role="img" aria-label="Five star marketplace rating badge"></div>
  <div class="trust-badge" style="width:70px" role="img" aria-label="Renewed marketplace badge"></div>
  <div class="trust-badge" style="width:92px" role="img" aria-label="Five star review badge"></div>
</div>

<h2 class="section-title quote-title">Select Your Device to Receive<br>an Instant Quote</h2>

<div class="device-grid">
  <a class="device-tile tile-slates"><div class="device-art" role="img" aria-label="Orvex tablet with colourful screen"></div><span>Slates</span></a>
  <a class="device-tile tile-desktops"><div class="device-art" role="img" aria-label="Orvex all-in-one desktop with colourful swirl screen"></div><span>Desktops</span></a>
  <a class="device-tile tile-notebooks"><div class="device-art" role="img" aria-label="Open Orvex notebook computer"></div><span>Notebooks</span></a>
  <a class="device-tile tile-phones"><div class="device-art" role="img" aria-label="Three Orvex phones showing home screens"></div><span>Phones</span></a>
</div>

<div class="works-backdrop" role="img" aria-label="Faint photo of devices and keyboard on a desk"></div>
<h2 class="section-title works-title">How It Works</h2>
<div class="steps">
  <div class="step">
    <svg viewBox="0 0 80 76"><rect x="8" y="4" width="64" height="46" rx="2"/><rect x="2" y="32" width="30" height="38" rx="2"/><rect x="58" y="42" width="18" height="30" rx="2"/><path d="M34 60h24M42 50v10M30 24l14-14M40 28l10-10M10 56l8-8M14 62l8-8"/></svg>
    <h3>Get An Offer</h3>
    <p>Lorem ipsum dolor sit amet, ea pro brute facer propriae nec epicurei senserit pericula cu. Ea graece animal equidem cum.</p>
  </div>
  <div class="step">
    <svg viewBox="0 0 80 76"><circle cx="40" cy="14" r="11"/><path d="M35 14l4 4 7-8M12 32l28-10 28 10-28 10zM12 32v30l28 11 28-11V32M40 42v31M12 32l-8 12 28 10 8-12M68 32l8 12-28 10-8-12M24 58l8 3M24 64h4"/></svg>
    <h3>Ship It Free</h3>
    <p>Facer propriae epicurei senserit pericula cu. Ea graece animal equidem cum. Ei graece omittantur vel.</p>
  </div>
  <div class="step">
    <svg viewBox="0 0 80 76"><rect x="64" y="8" width="10" height="20"/><rect x="4" y="50" width="10" height="20"/><path d="M64 12H46c-6 0-10 6-18 4l-12 10 6 4 12-8 6 4h10l14 2M14 54h16l16 8h10c4 0 4 6 0 6H40M14 66l16 4 30-8c6-2 8 4 2 6L34 74"/><circle cx="40" cy="32" r="8"/></svg>
    <h3>Get Paid Fast</h3>
    <p>Lorem ipsum dolor sit amet, ea pro brute facer propriae nec epicurei senserit pericula cu. Ei graece omittantur vel.</p>
  </div>
</div>

<footer class="site-footer">
  <div class="footer-dark"></div>
  <svg class="footer-red" width="1200" height="368" viewBox="0 0 1200 368"><polygon points="0,0 428,0 599,368 0,368" fill="#d01f2f"/></svg>
  <div class="brand"><div class="brand-square"></div>Pebble7dock</div>
  <div class="footer-col col-contact">
    <h4>Get In Touch</h4>
    <ul><li>Pebble7dock</li><li>48 Linden Row</li><li>Harbor Vale, NY, 10990</li><li>555-014-2297</li></ul>
  </div>
  <div class="footer-col col-support">
    <h4>Support</h4>
    <ul><li>Sell</li><li>Tracl</li><li>About Us</li><li>FAQs</li><li>Contact Us</li></ul>
  </div>
  <div class="footer-col col-legal">
    <h4>Legal</h4>
    <ul><li>Terms of Service</li><li>Privacy Policy</li><li>Contact Us</li></ul>
  </div>
  <p class="copyright">© 2019 – All rights reserved.</p>
  <div class="social" aria-label="Social links"><span></span><span></span><span></span></div>
</footer>

</body>
</html>
```